I need a logo design for a new company based in Tucson called "Mindpilot Reg Holloway". I am a psychotherapist that specializes in clinical psychology with athletes and performers. The final design should incorporate the psychology symbol as a watermark. The logo should convey movement and fluidity. "Mindpilot" is a bit of a play on words combining psychology (head) with sports (coach). Other design interests include mid-century, Ansel Brigham Kotter. I will want to use the logo for business cards, letterhead and marketing brochures. I will put together a website at a later date. I am attaching a file with some pertinent information for the business card. Thank you.
Reg Holloway
mindpilotregholloway@quillmarsh.net
Updates

Thank you all for the submissions so far.  I have submitted an additional file with a draft of a new design idea.  Since "mindpilot" is a bit of a play on words, I would like to see something with the two "H's" look something like quotation marks.  If the psychology logo is to be included at all, it needs to be less prominent.     Thank you all.  Reg                               

Target Market(s)

1) Adolescent and adult athletes and performers who are looking to increase their level of performance (Sport and Performance Psychology)
2) Adult psychotherapy patients (Clinical psychology)

Industry/Entity Type

Marketing

Colors

Designer to choose colors to be used in the design.

Requirements
Must have
• 1) Since "mindpilot" is a bit of a play on words, The "H's" need to be in a font that looks somewhat like quotation marks.

Nice to have
• Logo on one side. All other info on the backside?

```html
<!DOCTYPE html>
<html lang="en">
<head>
<meta charset="utf-8">
<title>Mindpilot — Business Card</title>
<link rel="stylesheet" href="https://fonts.googleapis.com/css2?family=Lato:wght@400;700&family=Marcellus&display=swap">
<style>
  :root {
    --backdrop: #d9d9d9;
    --card: #1f1f21;
    --teal: #7cc1b4;
    --white: #ffffff;
    --shadow: rgba(0,0,0,0.28);
  }
  * { margin: 0; padding: 0; box-sizing: border-box; }
  html, body {
    width: 1200px; height: 1000px; overflow: hidden;
    background: var(--backdrop);
  }
  .canvas { position: relative; width: 1200px; height: 1000px; }
  .card {
    position: absolute;
    width: 700px; height: 400px;
    background: var(--card);
    border-radius: 18px;
    box-shadow: 0 10px 30px var(--shadow);
    color: var(--teal);
  }
  .card--front { left: 80px; top: 70px; }
  .card--back  { left: 420px; top: 530px; }

  .brand {
    position: absolute; left: 70px; top: 110px; width: 560px;
  }
  .brand__name {
    display: flex; align-items: center; gap: 18px;
    font-family: "Lato", sans-serif; font-weight: 700;
    font-size: 92px; line-height: 1; color: var(--teal);
    letter-spacing: 2px;
  }
  .brand__mark {
    width: 26px; height: 26px; border-radius: 50%;
    background: var(--teal); flex: none;
  }
  .brand__tagline {
    margin-top: 22px;
    font-family: "Lato", sans-serif; font-weight: 700;
    font-size: 25px; letter-spacing: 2.5px;
    color: var(--white); text-transform: uppercase;
  }

  .contact { position: absolute; left: 0; right: 0; top: 40px; text-align: center; }
  .contact__name {
    font-family: "Marcellus", serif; font-size: 40px; letter-spacing: 1px;
  }
  .contact__title {
    font-family: "Lato", sans-serif; font-weight: 700; font-size: 17px;
    margin-top: 2px;
  }
  .contact__lines { margin-top: 26px; font-family: "Lato", sans-serif; font-weight: 700; }
  .contact__primary { font-size: 25px; line-height: 1.3; }
  .contact__secondary { font-size: 19px; line-height: 1.3; margin-top: 12px; }

  .card__blank {
    position: absolute; left: 70px; right: 70px; bottom: 30px; height: 78px;
    background: var(--white);
  }
</style>
</head>
<body>
<main class="canvas">
  <section class="card card--front" aria-label="Card front">
    <div class="brand">
      <div class="brand__name"><span class="brand__mark"></span>Mindpilot</div>
      <p class="brand__tagline">Clinical &amp; Performance Psychology</p>
    </div>
  </section>

  <section class="card card--back" aria-label="Card back">
    <div class="contact">
      <h1 class="contact__name">Reginald H. Holloway, MA, LLC</h1>
      <p class="contact__title">Licensed Professional Counselor</p>
      <div class="contact__lines">
        <p class="contact__primary">Mobile: 520.555.0187<br>mindpilotregholloway@quillmarsh.net</p>
        <p class="contact__secondary">4172 North Alder #204 Tucson,&nbsp; AZ 85716<br>Fax: 520.555.0342</p>
      </div>
    </div>
    <div class="card__blank"></div>
  </section>
</main>
</body>
</html>
```